Business Card Design

Massage therapy and healthy food
Zenova Health Massage (business name)

Target Market(s)

Health conscious

Industry/Entity Type

Business

Contact Information for Business Card

0413886207

Font styles to use
Serif

```html
<!DOCTYPE html>
<html lang="en">
<head>
<meta charset="utf-8">
<title>Zenova Health Massage Food – Business Card</title>
<link href="https://fonts.googleapis.com/css2?family=PT+Sans:ital,wght@0,400;0,700;1,700&display=swap" rel="stylesheet">
<style>
  :root {
    --page: #ffffff;
    --brand-green: #0d6a32;
    --leaf-green: #3f9a4c;
    --card-beige: #e4c3a6;
    --card-beige-light: #ead5bf;
    --card-lime: #a9d16e;
    --card-edge: #8c8c8c;
    --photo-warm: #c7a688;
    --photo-shadow: #6f5a4a;
  }
  * { box-sizing: border-box; margin: 0; padding: 0; }
  html, body {
    width: 1200px; height: 715px;
    overflow: hidden;
    background: var(--page);
  }
  .canvas {
    position: relative;
    width: 1200px; height: 715px;
    font-family: "PT Sans", Arial, sans-serif;
    color: var(--brand-green);
  }
  .card {
    position: absolute;
    border: 1.5px solid var(--card-edge);
    border-radius: 14px;
    overflow: hidden;
  }

  /* Back of card */
  .card--back {
    left: 515px; top: 1px;
    width: 684px; height: 401px;
    background: linear-gradient(90deg, var(--card-beige-light) 0%, #c9d69a 12%, var(--card-lime) 30%, var(--card-lime) 100%);
  }
  .card--back .brand-mark {
    position: absolute;
    left: 50%; top: 106px;
    width: 62px; height: 62px;
    margin-left: -31px;
    border-radius: 50%;
    background: var(--leaf-green);
  }
  .card--back .brand-name {
    position: absolute;
    left: 0; right: 0; top: 184px;
    text-align: center;
    font-size: 37px;
    font-weight: 700;
    letter-spacing: 0.2px;
  }

  /* Front of card */
  .card--front {
    left: 2px; top: 312px;
    width: 684px; height: 402px;
    background: var(--card-beige);
  }
  .photo-area {
    position: absolute;
    left: 0; top: 0;
    width: 312px; height: 100%;
    background:
      linear-gradient(90deg, rgba(228,195,166,0) 70%, var(--card-beige) 100%),
      linear-gradient(180deg, rgba(228,195,166,0.9) 0%, rgba(228,195,166,0) 14%, rgba(228,195,166,0) 86%, rgba(228,195,166,0.9) 100%),
      linear-gradient(160deg, var(--photo-warm) 0%, var(--photo-shadow) 45%, var(--photo-warm) 100%);
  }
  .card-info {
    position: absolute;
    left: 312px; right: 0; top: 0;
    text-align: center;
  }
  .card-info .brand-mark {
    position: absolute;
    left: 50%; top: 64px;
    width: 30px; height: 30px;
    margin-left: -30px;
    border-radius: 50%;
    background: var(--leaf-green);
  }
  .card-info .brand-name {
    position: absolute;
    left: -40px; right: 0; top: 104px;
    font-size: 18px;
    font-weight: 700;
  }
  .card-info .tagline {
    position: absolute;
    left: -40px; right: 0; top: 142px;
    font-size: 20px;
    font-weight: 400;
    color: var(--leaf-green);
  }
  .contact {
    position: absolute;
    left: -40px; right: 0; top: 222px;
    font-size: 42px;
    font-weight: 700;
    font-style: italic;
    line-height: 52px;
  }
</style>
</head>
<body>
  <div class="canvas">
    <section class="card card--back" aria-label="Card back">
      <span class="brand-mark" aria-hidden="true"></span>
      <h1 class="brand-name">Zenova Health Massage Food</h1>
    </section>

    <section class="card card--front" aria-label="Card front">
      <div class="photo-area" role="img" aria-label="Photo of a chef slicing fresh fruit on a wooden board"></div>
      <div class="card-info">
        <span class="brand-mark" aria-hidden="true"></span>
        <h2 class="brand-name">Zenova Health Massage Food</h2>
        <p class="tagline">Massage therapy and healthy food</p>
        <p class="contact">Contact<br>0413886207</p>
      </div>
    </section>
  </div>
</body>
</html>
```